依頼詳細
会社の封筒デザインを依頼します。封筒は「シンプル」だけど「先進的」なデザインを希望します。封筒は淡い水色です。発注先の印刷会社さんはグラデーションがあるとコスト高になりますので、グラデーションは入れないでください。また、黒1色で考えておりますので宜しくお願いします。
長3の封筒は横むきでお願いします。
記載項目
表面:会社名/〒住所/電話/Fax/URL
サイズ
希望イメージ
• +5 0 +5
• シンプル
複雑
• 単色
カラフル
• 暗い
明るい
• 日常
高級
• 遊び心
厳粛
• 未来的
伝統的
• 女性的
男性的
納品ファイル
• 高解像度JPG (.jpg)
• イラストレーター形式 (.ai)
補足説明
住所や氏名を記載する場合の下線を薄めか、点線で入れ、端に御中の文字を入れて下さい。
依頼公開後の追記内容
ロゴデータ追加致しました
ファイルの追加が出来ていませんでしたので、再度投稿しました。
【イメージの追記】
イメージですが、透き通ったような?スタイリッシュな?都会的な?繊細な?
簡単にいうと、かっこいい?ようなイメージでお願いできたらと思います。
言葉で伝えるって難しいですね。
表現力が無くてすみません。

申し訳ございませんが、締切日を延期させていただきました。
これまでご提案下さいました方には、ご了承の程宜しくお願い致します。
■ 選んだ理由

シンプルで、弊社のイメージしていたものを表現してくれたようなデザインでした。

■ 提案者全員のお礼・コメント

どれもこれも素敵なデザインばかりで選ぶのが大変でした。
皆様のデザインに感謝いたします。ありがとうございました。
今後も、機会がございましたら、宜しくお願い致します。

```html
<!DOCTYPE html>
<html lang="ja">
<head>
<meta charset="utf-8">
<title>霧沢製作所 封筒</title>
<link href="https://fonts.googleapis.com/css2?family=Roboto:wght@700&family=Noto+Sans+JP:wght@400;700&display=swap" rel="stylesheet">
<style>
  :root {
    --paper: #e4eff7;
    --paper-edge: #b9c6cf;
    --flap-dark: #8f9397;
    --flap-light: #b4b7ba;
    --ink: #1e1e1e;
    --rule: #7d8a94;
    --sub-ink: #444;
  }
  html, body {
    margin: 0;
    width: 800px;
    height: 1200px;
    overflow: hidden;
    background: #ffffff;
  }
  .envelope {
    position: relative;
    width: 800px;
    height: 1200px;
    background: var(--paper);
    box-sizing: border-box;
    border: 2px solid var(--paper-edge);
    font-family: "Noto Sans JP", sans-serif;
    color: var(--ink);
  }
  .flap {
    position: absolute;
    left: 0; top: 0;
    width: 100%;
    height: 125px;
  }
  .flap-brand {
    position: absolute;
    left: 0; right: 0;
    top: 22px;
    text-align: center;
    transform: rotate(180deg);
    color: #ffffff;
    font-family: "Roboto", sans-serif;
    font-weight: 700;
    line-height: 1.1;
  }
  .flap-brand .name { font-size: 30px; letter-spacing: 1px; display: block; }
  .flap-brand .tag { font-size: 12px; display: block; }
  .address-lines {
    position: absolute;
    left: 100px;
    top: 300px;
  }
  .address-line {
    height: 58px;
    border-bottom: 2px dotted var(--rule);
    width: 375px;
    box-sizing: border-box;
  }
  .address-line.recipient {
    width: 450px;
    position: relative;
  }
  .onchu {
    position: absolute;
    left: 458px;
    bottom: -6px;
    font-size: 22px;
    font-weight: 700;
    white-space: nowrap;
  }
  .sender {
    position: absolute;
    left: 52px;
    top: 1022px;
  }
  .brand {
    display: flex;
    align-items: center;
    gap: 10px;
    font-family: "Roboto", sans-serif;
    font-weight: 700;
    color: var(--ink);
  }
  .brand-dot {
    width: 50px; height: 50px;
    border-radius: 50%;
    background: var(--ink);
  }
  .brand-text { line-height: 1.05; }
  .brand-text .name { font-size: 38px; display: block; letter-spacing: 0.5px; }
  .brand-text .tag { font-size: 15px; display: block; padding-left: 40px; }
  .company {
    margin-top: 24px;
    font-size: 15px;
    font-weight: 700;
  }
  .contact {
    margin-top: 6px;
    font-size: 11px;
    color: var(--sub-ink);
    white-space: nowrap;
    letter-spacing: 0.2px;
  }
  .contact span + span { margin-left: 10px; }
</style>
</head>
<body>
<div class="envelope">
  <svg class="flap" viewBox="0 0 800 125" aria-hidden="true">
    <polygon points="0,0 800,0 800,78 740,122 60,122 0,78" fill="var(--flap-light)"/>
    <rect x="0" y="0" width="800" height="78" fill="var(--flap-dark)"/>
  </svg>
  <div class="flap-brand">
    <span class="name">KIRISAWA</span>
    <span class="tag">Coating Company</span>
  </div>

  <div class="address-lines">
    <div class="address-line"></div>
    <div class="address-line"></div>
    <div class="address-line"></div>
    <div class="address-line recipient"><span class="onchu">御中</span></div>
  </div>

  <div class="sender">
    <div class="brand">
      <div class="brand-dot"></div>
      <div class="brand-text">
        <span class="name">KIRISAWA</span>
        <span class="tag">Coating Company</span>
      </div>
    </div>
    <div class="company">有限会社 霧沢製作所</div>
    <div class="contact">
      <span>〒370-0000 群馬県架空市青葉町 1-2</span>
      <span>TEL 0270-00-1234</span>
      <span>FAX 0270-00-1235</span>
      <span>http://www.kirisawa-coat.example.jp</span>
    </div>
  </div>
</div>
</body>
</html>
```